Elegant and modern Wedding Photography brochure

My existing brochure (attached) needs a major facelift. This is one of the main selling tools - it gets emailed to my clients when they make an equiry on what packages i offer and it is printed out and walked through at our first meeting. This brochure is as critical as my website - it needs to sing!

I'm looking for an eye-catching design that says:
Elegant
Modern
Clean
Crisp
Not cutesy or lovey-dovey thanks - we are more sophisticated and professional than that.

Update images to some of the latest weddings I've shot also. Let me know files and resolution you need. I've enabled right-click to download images on my site for a limited time. Please note that I retain copyright and will pursue any breeches.

Http://www.clarapennock.com/Melbourne-wedding-photography
Updates

Thanks for all of your designs! Will take a few days to decide.

Target Market(s)

Australian Women aged 24-44

Industry/Entity Type

Wedding

Font styles to use
Other font styles liked:
• Century Gothic

Requirements
Must have
• Easy to print - does not have to be 6 A4 pages like the existing brochure
Nice to have
• Some full page images - The photos are supposed to be the hero here :-)
Should not have
• Not cutesy or lovey-dovey thanks - we are more sophisticated and professional than that.

No black backgrounds, I prefer a white thanks

No images in organic shaped boxes (like the rectangles in the logo - no thanks).
Keep the lines straight and sharp

```html
<!DOCTYPE html>
<html lang="en">
<head>
<meta charset="utf-8">
<title>Wedding Packages – Pricelist 2013</title>
<link rel="stylesheet" href="https://fonts.googleapis.com/css2?family=Didact+Gothic&display=swap">
<style>
  :root {
    --paper: #ffffff;
    --salmon: #e3937b;
    --salmon-body: #e5977f;
    --teal: #6f9ea4;
    --sand: #cfc6b3;
    --sand-head: #d3cbbb;
    --red: #c23a2c;
    --grey: #7d7d7d;
    --sand-text: #a89a80;
    --white: #ffffff;
  }
  * { box-sizing: border-box; margin: 0; padding: 0; }
  html, body { width: 848px; height: 1200px; overflow: hidden; background: var(--paper); }
  body { font-family: "Didact Gothic", "Century Gothic", sans-serif; position: relative; }

  .page-title {
    position: absolute; top: 26px; left: 0; width: 848px; text-align: center;
    font-size: 50px; font-weight: 400; letter-spacing: 1px; color: var(--salmon);
  }
  .page-subtitle {
    position: absolute; top: 94px; left: 0; width: 848px; text-align: center;
    font-size: 25px; color: var(--grey);
  }

  .package { position: absolute; top: 146px; width: 262px; }
  .package--signature { left: 22px; }
  .package--platinum { left: 294px; }
  .package--gold { left: 566px; }

  .package-name {
    height: 42px; line-height: 42px; text-align: center; font-size: 32px; font-weight: 400;
  }
  .package--signature .package-name { background: var(--teal); color: #e7e1d4; }
  .package--platinum .package-name { background: var(--salmon); color: var(--teal); }
  .package--gold .package-name { background: var(--sand-head); color: var(--red); }

  .package-body { position: relative; margin-top: 10px; height: 788px; overflow: hidden; }
  .package--signature .package-body { background: var(--sand); }
  .package--platinum .package-body { background: var(--teal); }
  .package--gold .package-body { background: var(--salmon-body); }

  .features {
    list-style: none; color: var(--white); font-size: 15px; line-height: 27px;
    padding: 18px 8px 0 10px; letter-spacing: 0.3px;
  }
  .features li { padding-left: 9px; text-indent: -9px; }
  .features li::before { content: "•"; margin-right: 2px; }
  .package--platinum .features { padding-top: 0; position: absolute; top: 328px; }

  .photo { position: absolute; left: 0; width: 262px; }
  .photo--arch { top: 510px; height: 278px;
    background: linear-gradient(180deg, #c9bda6 0%, #a5977d 45%, #6f6353 100%); }
  .photo--shoes { top: 0; height: 318px;
    background: linear-gradient(180deg, #3a3a3a 0%, #cfd3d3 30%, #e9eceb 60%, #8fb0b4 100%); }
  .photo--couple { top: 282px; height: 506px;
    background: linear-gradient(180deg, #e7a58e 0%, #d99a80 40%, #b47d62 75%, #8e6a52 100%); }

  .price {
    position: absolute; top: 988px; width: 262px; text-align: center;
    font-size: 15px; line-height: 19px;
  }
  .price--signature { left: 22px; color: var(--sand-text); }
  .price--platinum { left: 294px; color: var(--teal); }
  .price--gold { left: 566px; color: var(--red); }

  .footnote {
    position: absolute; top: 1151px; left: 0; width: 848px; text-align: center;
    font-size: 15px; color: var(--grey); letter-spacing: 0.3px;
  }
</style>
</head>
<body>
  <h1 class="page-title">Wedding Packages</h1>
  <p class="page-subtitle">Pricelist 2013</p>

  <section class="package package--signature">
    <h2 class="package-name">Signature</h2>
    <div class="package-body">
      <ul class="features">
        <li>Up to 8 hrs of coverage</li>
        <li>Signature Grand (A3) Album with Lay-flat 300g paper, frosted page, choice of premium linen or leather&nbsp; cover, presentation box, name embossing, up to 52 pages</li>
        <li>Custom Thank-you Cards with envelopes (50)</li>
        <li>Client for life (no sitting fees)</li>
        <li>Second photographer</li>
        <li>Fusion Slideshow (still + moving images)</li>
        <li>Pre-wedding Shoot</li>
        <li>Web Gallery (online for 6 weeks) &amp; Social media</li>
        <li>High Resolution Digital Negatives*</li>
      </ul>
      <div class="photo photo--arch" role="img" aria-label="Couple embracing beneath a sandstone archway"></div>
    </div>
  </section>

  <section class="package package--platinum">
    <h2 class="package-name">Platinum</h2>
    <div class="package-body">
      <div class="photo photo--shoes" role="img" aria-label="Bridal shoes and perfume beneath a crystal lamp"></div>
      <ul class="features">
        <li>Up to 6 hrs of coverage</li>
        <li>Regular (A4) Album with Lay-flat 300g paper, printed cover, dust jacket, presentation box, up to 42 pages</li>
        <li>Slideshow</li>
        <li>Pre-wedding shoot</li>
        <li>Web Gallery (online for 6 weeks) &amp; Social media</li>
        <li>High Resolution Digital Negatives*</li>
      </ul>
    </div>
  </section>

  <section class="package package--gold">
    <h2 class="package-name">Gold</h2>
    <div class="package-body">
      <ul class="features">
        <li>Up to 4 hrs of coverage</li>
        <li>Regular (A4) Album with Lay-flat 300g paper, printed cover, dust jacket, presentation box, up to 32 pages</li>
        <li>Web Gallery (online for 6 weeks)</li>
        <li>High Resolution Digital Negatives*</li>
      </ul>
      <div class="photo photo--couple" role="img" aria-label="Couple kissing under a tree in warm sunlight"></div>
    </div>
  </section>

  <p class="price price--signature">Price: $3650<br>($5540 value)</p>
  <p class="price price--platinum">Price: $2300<br>($3440 value)</p>
  <p class="price price--gold">Price: $1650<br>($2080 value)</p>

  <p class="footnote">* Approx. 1200x1800 jpeg at 240 pixels per inch. Suitable for prints up to 8x10inch. No watermarks</p>
</body>
</html>
```